Web Design Project

Revamp current website adding newly designed logo and creating layout that is good on desktops, tablets, and cell phones.

Current website can be viewed at www.venkirainteriors.com

Will you see the website is small but graphics heavy in the gallery. The gallery needs to be setup so that it is easy to maintain the links and update the photos.

Needs to have high visual impact.

I need a new logo and website layout designed for my partner's business. This is a birthday present. His business is interior painting, wallpapering and design. He also has access to a wide variety of products including carpet, fabrics, furniture, wallpaper, tile, countertops, etc. I have attached some screen shots of his website for reference. He is a one man shop and has a stellar reputation with his customers. He is on-time, very tidy, excellent with animals, and always finishes on time and on budget. There are no restrictions on colors or fonts. The logo needs to work well with the website, business cards and printed materials. The website needs to flow content for device size so it looks just as good on a cell phone or tablet as it does on a desktop computer. Whatever the heck that's called! Thanks. I am looking forward to seeing everyone's ideas.

Target Market(s)

Consumers looking for interior design, painting, and wallpapering as well as interior products such as flooring, window treatments, reupholstering, counter tops, etc.

Industry/Entity Type

Cell Phone

Requirements
Must have
• Clean, sharp, visual impact (at least on the home page)
Should not have
• Clutter.

```html
<!DOCTYPE html>
<html lang="en">
<head>
<meta charset="utf-8">
<title>Venkira Interior Designs</title>
<link rel="stylesheet" href="https://fonts.googleapis.com/css2?family=Libre+Baskerville&family=Merriweather:ital,wght@0,300;1,300&family=Montserrat:wght@400;700&display=swap">
<style>
  :root {
    --brand-red: #c8102e;
    --ink: #2b2b2b;
    --muted: #6b6b6b;
    --rule: #e6e6e6;
    --panel: #f3f3f1;
    --page: #ffffff;
    --room-wall: #ece7b8;
    --room-wood: #c89a62;
    --stone: #cfc6b6;
    --can-green: #5f7a2e;
  }
  * { box-sizing: border-box; margin: 0; padding: 0; }
  html, body { width: 1200px; height: 686px; overflow: hidden; background: var(--page); }
  body { position: relative; font-family: "Merriweather", Georgia, serif; color: var(--ink); }

  .page-frame {
    position: absolute; left: 150px; top: 0; width: 900px; height: 686px;
    border-left: 1px solid var(--rule); border-right: 1px solid var(--rule);
  }

  .site-header { position: absolute; left: 170px; top: 26px; width: 860px; text-align: center; }
  .site-name {
    font-family: "Libre Baskerville", Georgia, serif; font-weight: 400;
    font-size: 30px; color: var(--brand-red); letter-spacing: 0.2px;
  }

  .main-nav {
    position: absolute; left: 370px; top: 80px; width: 460px; height: 34px;
    border-top: 1px solid var(--rule); border-bottom: 1px solid var(--rule);
    display: flex; justify-content: space-between; align-items: center; padding: 0 14px;
  }
  .main-nav a {
    font-family: "Montserrat", Arial, sans-serif; font-size: 9px; letter-spacing: 1.6px;
    text-transform: uppercase; color: var(--ink); text-decoration: none;
  }
  .main-nav a.is-current { color: var(--brand-red); }

  .hero { position: absolute; left: 170px; top: 132px; width: 860px; height: 290px; display: flex; gap: 10px; }
  .hero-photo { height: 100%; }
  .hero-photo--studio { width: 545px; background: linear-gradient(180deg, var(--room-wall) 0%, #e8dfb0 55%, var(--room-wood) 100%); }
  .hero-photo--fireplace { flex: 1; background: linear-gradient(90deg, var(--stone) 0%, #bdb3a1 55%, #a87a4d 100%); }

  .welcome { position: absolute; left: 170px; top: 446px; width: 600px; }
  .welcome-title {
    font-family: "Montserrat", Arial, sans-serif; font-weight: 700; font-size: 11px;
    letter-spacing: 0.6px; text-transform: uppercase; margin-bottom: 12px;
  }
  .welcome-product {
    float: left; width: 62px; height: 86px; margin: 4px 20px 6px 0;
    background: linear-gradient(180deg, #e2c63a 0%, var(--can-green) 60%, #3f5220 100%);
    border-radius: 3px;
  }
  .welcome-copy { font-size: 11.5px; font-weight: 300; line-height: 21px; }

  .testimonial {
    position: absolute; left: 800px; top: 446px; width: 230px; height: 240px;
    background: var(--panel); padding: 18px 20px; text-align: center;
  }
  .quote-mark { display: block; margin: 0 auto 10px; }
  .testimonial-avatar {
    width: 58px; height: 58px; border-radius: 50%; margin: 0 auto 14px;
    background: linear-gradient(180deg, #d9d0bd, #a89a7e); border: 3px solid #fff;
  }
  .testimonial-text { font-size: 10px; font-style: italic; font-weight: 300; line-height: 17px; color: var(--muted); text-align: left; }
  .testimonial-name { margin-top: 10px; font-size: 10px; color: var(--ink); text-align: left; }
</style>
</head>
<body>
  <div class="page-frame"></div>

  <header class="site-header">
    <h1 class="site-name">Venkira Interior Designs</h1>
  </header>

  <nav class="main-nav">
    <a class="is-current" href="#">Home</a>
    <a href="#">About</a>
    <a href="#">Gallery</a>
    <a href="#">Products</a>
    <a href="#">Services</a>
    <a href="#">Contact</a>
  </nav>

  <section class="hero">
    <div class="hero-photo hero-photo--studio" role="img" aria-label="Photo of a bright studio with wooden desks, shelves and a wall clock"></div>
    <div class="hero-photo hero-photo--fireplace" role="img" aria-label="Photo of a living room with a stone fireplace and a carved wooden cabinet"></div>
  </section>

  <section class="welcome">
    <h2 class="welcome-title">Welcome to Venkira Interior Designs.</h2>
    <div class="welcome-product" role="img" aria-label="Photo of a can of interior paint"></div>
    <p class="welcome-copy">With the various materials, colors, and finishes available the choices today can be daunting. By listening to you, I am able to pick just the right color, the right fabric, or the right furniture for your projects. Whether you are starting with a small project or a large project, I am ready to bring your ideas to life. It doesn't take a big budget to achieve dramatic effects. A wonderful new look is within anyone's reach. My guidance with the selection of colors, fabrics, paint, wallpaper, and furniture, as well as the placement of items in a room, will help you achieve the results you desire – a beautiful home that is a joy to walk into and to show off!</p>
  </section>

  <aside class="testimonial">
    <svg class="quote-mark" width="22" height="22" viewBox="0 0 22 22" aria-hidden="true">
      <circle cx="11" cy="11" r="10" fill="none" stroke="#555" stroke-width="1"/>
      <text x="11" y="17" text-anchor="middle" font-family="Georgia, serif" font-size="14" fill="#555">”</text>
    </svg>
    <div class="testimonial-avatar" role="img" aria-label="Portrait photo of the client"></div>
    <p class="testimonial-text">Venkira made our den feel brand new. It's like a dream come true, though I worried about the cost. I feel myself relax every evening and recommend him to all.</p>
    <p class="testimonial-name">Maren</p>
  </aside>
</body>
</html>
```